Modern Minimalistic Supplement Label

Opportunity for recurring projects with a growing company. We have provided a detailed creative brief and all necessary files and guidelines. If you have any questions we will be closely monitoring the discussion board and email provided.

THE NAMES LISTED IN THE BRIEF ARE DIFFERENT FROM THE LABEL TEMPLATES. This is a private label brand. The label templates given are generic so please examine the entire brief before starting.

Use the PSD mockups attached and pair the labels with the correct bottles.

Do not use an entirely white background.

This could be excellent portfolio material.

Start by looking at the "CREATIVE_BRIEF" file. Logo files are contained in the "67046451" zip file.

UPDATE* Use the following business address for the "manufactured for" box on the labels.

Bramwell
4817 Pelton Ave. #2096
Ann Arbor MI 48276

Target Market(s)

All information provided in "CREATIVE_BRIEF" file.

Industry/Entity Type

Supplement

Requirements
Must have
• All information provided in "CREATIVE_BRIEF" file.
Nice to have
Should not have

```html
<!DOCTYPE html>
<html lang="en">
<head>
<meta charset="utf-8">
<title>Bramwell Amino – Raspberry Iced Tea Label</title>
<link rel="stylesheet" href="https://fonts.googleapis.com/css2?family=Open+Sans:wght@400;600;700&family=Lato:wght@400;700&display=swap">
<style>
  :root {
    --backdrop: #e6e6e8;
    --label-white: #ffffff;
    --ink: #1d1d1f;
    --ink-soft: #3a3a3d;
    --brand-band: #161616;
    --accent-red: #a3262f;
    --mist-blue: #9fb6d6;
    --mist-pale: #dbe5f1;
  }
  html, body {
    margin: 0;
    padding: 0;
    width: 1200px;
    height: 1200px;
    overflow: hidden;
    background: var(--backdrop);
  }
  .canvas {
    position: relative;
    width: 1200px;
    height: 1200px;
    background: radial-gradient(circle at 50% 40%, #f4f4f5 0%, var(--backdrop) 75%);
  }
  .label {
    position: absolute;
    left: 180px;
    top: 150px;
    width: 840px;
    height: 900px;
    background: var(--label-white);
    box-shadow: 0 10px 40px rgba(0, 0, 0, 0.08);
    overflow: hidden;
  }
  .brand-band {
    position: absolute;
    left: 183px;
    top: 40px;
    width: 474px;
    height: 250px;
    background: var(--brand-band);
    display: flex;
    align-items: flex-end;
    justify-content: center;
    padding-bottom: 40px;
    box-sizing: border-box;
  }
  .brand-name {
    font-family: "Open Sans", sans-serif;
    font-weight: 600;
    font-size: 62px;
    letter-spacing: 4px;
    color: #ffffff;
    line-height: 1;
  }
  .mist-scene {
    position: absolute;
    left: 0;
    top: 300px;
    width: 840px;
    height: 330px;
    background:
      linear-gradient(180deg, rgba(255,255,255,0) 0%, var(--mist-pale) 30%, var(--mist-blue) 60%, var(--mist-pale) 82%, rgba(255,255,255,0) 100%);
    opacity: 0.85;
  }
  .product-name {
    position: absolute;
    left: 0;
    top: 300px;
    width: 840px;
    text-align: center;
    font-family: "Open Sans", sans-serif;
    font-weight: 400;
    font-size: 232px;
    line-height: 1;
    letter-spacing: -2px;
    color: var(--ink);
    -webkit-text-stroke: 4px var(--accent-red);
    paint-order: stroke fill;
    margin: 0;
    white-space: nowrap;
  }
  .flavor {
    position: absolute;
    left: 0;
    top: 548px;
    width: 840px;
    text-align: center;
    font-family: "Open Sans", sans-serif;
  }
  .flavor-name {
    font-size: 32px;
    font-weight: 400;
    color: var(--ink);
    letter-spacing: 1px;
    line-height: 1.15;
  }
  .flavor-note {
    font-size: 13px;
    color: var(--ink-soft);
    line-height: 1.3;
    margin-top: 2px;
  }
  .category {
    position: absolute;
    left: 0;
    top: 660px;
    width: 840px;
    text-align: center;
    font-family: "Lato", sans-serif;
    font-weight: 400;
    font-size: 44px;
    letter-spacing: 6px;
    color: var(--accent-red);
    white-space: nowrap;
  }
  .net-weight {
    position: absolute;
    right: 40px;
    top: 780px;
    font-family: "Lato", sans-serif;
    font-weight: 700;
    font-size: 20px;
    letter-spacing: 2px;
    color: var(--ink-soft);
  }
</style>
</head>
<body>
  <main class="canvas">
    <section class="label">
      <div class="brand-band">
        <span class="brand-name">BRAMWELL</span>
      </div>
      <div class="mist-scene" role="img" aria-label="Soft blue watercolor mountain range behind the product name"></div>
      <h1 class="product-name">Amino</h1>
      <div class="flavor">
        <div class="flavor-name">Raspberry Iced Tea</div>
        <div class="flavor-note">Natural &amp; Artificial Flavor</div>
      </div>
      <div class="category">DIETARY SUPPLEMENT</div>
      <div class="net-weight">NET WT. 360 g</div>
    </section>
  </main>
</body>
</html>
```